Business card design needed

I am a nutritionist and fitness instructor and I need a business card designed for my company CookRunGrow. I provide nutrition education services such as consultations, cooking demonstrations, workshops, and supermarket tours. I also provide fitness instruction and training to clients to help overhaul their lifestyle.

I would like to see designs that have a natural, organic, feel using earthy colours. I would like to have cards printed on recycled paper.

I would prefer a 2 sided card. Front side with just the business name Cook Run Grow and underneath Nutrition Health Fitness. The second side to have the contact details.

The final design should communicate health and wellness through eating organic wholefoods and being physically active.

Although I have this idea, I would be open to see other suggestions that have a similar look and feel.

Target Market(s)

people interested in being healthier, women wanting to loose weight, mothers wanting to be healthier for their families

Industry/Entity Type

Nutrition

Contact Information for Business Card

Megan Furlow
Nutritionist and Personal Trainer
M 0417382956
E cookrungrowwellness@mailbox-demo.net

Logo Text

CookRunGrow (underneath) Nutrition Health Fitness

Logo styles of interest
Wordmark Logo
Requirements
Nice to have
• I like the idea of having the letters of CookRunGrow spelt out with food such as grains, nuts, seeds, legumes, fruit etc. For example close up images of cherry tomatoes, chia seeds, kidney beans, chickpeas, blue berries, raspberries, brown rice - lots of different colours and textures. Continuing playing on the idea of the book cover Walk Sing Rest.

food is important - I am not selling supplements rather I am promoting the enjoyment of healthy wholefoods so food is important to the look and feel of the design
Should not have
• cartoon images
images associated with body building or supplements
fruit or dumb bells with tape measures around them
clichés for weight loss such as scales and tape measures
I don't want to look like other typical wellness services such as massage or spa services

```html
<!DOCTYPE html>
<html lang="en">
<head>
<meta charset="utf-8">
<title>CookRunGrow – Business Card</title>
<link rel="stylesheet" href="https://fonts.googleapis.com/css2?family=Mulish:wght@400;700&display=swap">
<style>
  :root {
    --backdrop: #e8e9e9;
    --paper: #efe8b6;
    --leaf: #2e5d1c;
    --rule: #4f7a2a;
    --ink: #2f2f2f;
    --ink-soft: #474747;
  }
  * { box-sizing: border-box; margin: 0; padding: 0; }
  html, body {
    width: 1029px;
    height: 1200px;
    overflow: hidden;
    background: var(--backdrop);
    font-family: "Mulish", "Century Gothic", sans-serif;
  }
  .card {
    position: absolute;
    width: 872px;
    height: 502px;
    border-radius: 32px;
    background: var(--paper);
    box-shadow: 0 3px 10px rgba(0,0,0,0.25);
  }
  .card--front { left: 68px; top: 65px; }
  .card--back  { left: 81px; top: 629px; }

  /* Front */
  .wordmark {
    position: absolute;
    left: 0; right: 0;
    top: 146px;
    text-align: center;
    font-size: 88px;
    font-weight: 700;
    line-height: 1;
    color: var(--leaf);
  }
  .tagline {
    position: absolute;
    left: 46px; right: 66px;
    top: 272px;
    display: flex;
    align-items: center;
    gap: 6px;
  }
  .tagline__rule {
    flex: 1;
    height: 4px;
    background: var(--rule);
  }
  .tagline__text {
    font-size: 28px;
    font-weight: 700;
    color: var(--leaf);
    white-space: nowrap;
  }

  /* Back */
  .brand-name {
    position: absolute;
    left: 100px;
    width: 210px;
    top: 213px;
    text-align: right;
    font-size: 31px;
    font-weight: 700;
    line-height: 1;
    color: var(--leaf);
    white-space: nowrap;
  }
  .divider {
    position: absolute;
    left: 324px;
    top: 148px;
    width: 4px;
    height: 171px;
    background: var(--rule);
  }
  .contact {
    position: absolute;
    left: 347px;
    top: 146px;
  }
  .contact__name {
    font-size: 22px;
    font-weight: 700;
    color: var(--ink);
    line-height: 1.2;
  }
  .contact__role {
    font-size: 25px;
    font-weight: 400;
    color: var(--ink-soft);
    line-height: 1.2;
  }
  .contact__line {
    display: flex;
    align-items: center;
    gap: 14px;
    font-size: 21px;
    font-weight: 700;
    color: var(--ink);
    white-space: nowrap;
  }
  .contact__line--phone { margin-top: 34px; }
  .contact__line--mail { margin-top: 22px; font-size: 20px; }
  .contact__icon { width: 24px; height: 24px; flex: none; }
</style>
</head>
<body>
  <section class="card card--front" aria-label="Card front">
    <h1 class="wordmark">CookRunGrow</h1>
    <div class="tagline">
      <span class="tagline__rule"></span>
      <span class="tagline__text">Nutrition Health Fitness</span>
      <span class="tagline__rule"></span>
    </div>
  </section>

  <section class="card card--back" aria-label="Card back">
    <p class="brand-name">CookRunGrow</p>
    <div class="divider"></div>
    <div class="contact">
      <p class="contact__name">Megan Furlow</p>
      <p class="contact__role">Nutritionist and Personal Trainer</p>
      <p class="contact__line contact__line--phone">
        <svg class="contact__icon" viewBox="0 0 24 24" aria-hidden="true">
          <rect x="6" y="2" width="12" height="20" rx="2" fill="none" stroke="#2f2f2f" stroke-width="2"/>
          <line x1="10" y1="18.5" x2="14" y2="18.5" stroke="#2f2f2f" stroke-width="1.6"/>
        </svg>
        0417382956
      </p>
      <p class="contact__line contact__line--mail">
        <svg class="contact__icon" viewBox="0 0 24 24" aria-hidden="true">
          <rect x="2" y="5" width="20" height="14" fill="none" stroke="#2f2f2f" stroke-width="2"/>
          <polyline points="2,5 12,13 22,5" fill="none" stroke="#2f2f2f" stroke-width="2"/>
        </svg>
        cookrungrowwellness@mailbox-demo.net
      </p>
    </div>
  </section>
</body>
</html>
```